IT solutions & services company requires stationary makeover

Looking for a consistent modern, professional design across our printed client touch points:
Business Cards
Letterhead
Client proposal
Flyer
Postcard

We provide solutions for SME IT - servers, backups, AV etc, and the ongoing services around them.
we are happy with our logo - please see attached and would like the colour theme to be maintained.

```html
<!DOCTYPE html>
<html lang="en">
<head>
<meta charset="utf-8">
<title>Nexora Stationery Set</title>
<link rel="stylesheet" href="https://fonts.googleapis.com/css2?family=Montserrat:wght@400;600;700&family=Open+Sans:wght@400;600&display=swap">
<style>
  :root{
    --blue:#1b8fc6;
    --blue-deep:#0b84b6;
    --blue-soft:#63b5dc;
    --ink:#161616;
    --paper:#ffffff;
    --stage:#ebebeb;
    --grey-text:#555;
    --faint:#eeeeee;
  }
  *{box-sizing:border-box;margin:0;padding:0}
  html,body{width:1200px;height:795px;overflow:hidden}
  body{background:var(--stage);font-family:"Open Sans",Arial,sans-serif;color:var(--ink);position:relative}
  .sheet{position:absolute;background:var(--paper);box-shadow:0 2px 6px rgba(0,0,0,.12);overflow:hidden}

  /* brand name lockup */
  .brand{position:absolute;display:flex;align-items:center;gap:6px;font-family:"Montserrat",sans-serif;font-weight:600;color:var(--ink);line-height:1}
  .brand-dot{border-radius:50%;background:var(--blue)}
  .brand--light{color:var(--paper)}
  .brand--light .brand-dot{background:var(--paper)}

  .contact{position:absolute;list-style:none;font-size:6px;line-height:10px;color:var(--grey-text)}
  .contact li{display:flex;align-items:center;gap:4px}
  .contact li::before{content:"";width:4px;height:4px;background:var(--blue);flex:none}
  .contact--light{color:#e6e6e6}

  .person-name{position:absolute;font-family:"Montserrat",sans-serif;font-weight:600;color:var(--blue);font-size:11px}
  .person-role{position:absolute;font-size:6px;color:var(--grey-text)}

  /* business cards */
  .card{width:260px;height:149px;left:40px}
  .card--front{top:70px}
  .card--dark{top:239px;background:var(--ink)}
  .card--blue{top:408px;background:var(--blue)}
  .card--back{top:577px}

  /* documents */
  .doc{width:257px;height:364px;top:215px}
  .letterhead{left:340px}
  .cover{left:621px}
  .flyer{left:902px}

  .faint-mark{position:absolute;border-radius:50%}

  .cover-panel{position:absolute;left:0;top:0;width:100%;height:272px;background:var(--blue-deep)}
  .cover-title{position:absolute;left:124px;top:150px;font-family:"Montserrat",sans-serif;font-weight:600;color:var(--paper);font-size:15px;line-height:1.1}
  .cover-sub{position:absolute;left:124px;top:170px;font-size:5.5px;color:#dff0f8}
  .cover-date{position:absolute;right:20px;top:196px;font-family:"Montserrat",sans-serif;color:var(--paper);font-size:10px;letter-spacing:1px}

  .flyer-title{position:absolute;right:18px;top:70px;font-family:"Montserrat",sans-serif;font-weight:700;color:var(--blue);font-size:14px}
  .flyer-sub{position:absolute;right:18px;top:89px;font-size:5px;color:var(--grey-text)}
  .flyer-body{position:absolute;left:18px;right:18px;top:118px;font-size:5.3px;line-height:7.2px;color:#222;text-align:justify}
  .flyer-body p+p{margin-top:6px}
  .rule{position:absolute;height:1px;background:var(--blue)}
  .footer-line{position:absolute;display:flex;gap:14px;font-size:5px;color:var(--grey-text)}
  .footer-line span::before{content:"";display:inline-block;width:4px;height:4px;background:var(--blue);margin-right:3px;vertical-align:middle}
</style>
</head>
<body>

<!-- white card front -->
<section class="sheet card card--front" aria-label="Business card front">
  <div class="brand" style="left:62px;top:60px;font-size:26px"><span class="brand-dot" style="width:20px;height:20px"></span>nexora</div>
</section>

<!-- dark card -->
<section class="sheet card card--dark" aria-label="Business card back, dark">
  <div class="faint-mark" role="img" aria-label="Brand symbol decoration" style="left:24px;top:34px;width:78px;height:78px;background:radial-gradient(circle at 40% 35%,#4fb4e4,#0b5f8a)"></div>
  <div class="person-name" style="left:128px;top:26px">Adrian Vale</div>
  <div class="person-role" style="left:128px;top:41px;color:#bbb">Managing Director</div>
  <ul class="contact contact--light" style="left:128px;top:68px">
    <li>+1 (555) 014 2290</li>
    <li>+1 (555) 014 2291</li>
    <li>hello@nexora-it.com</li>
    <li>48 Harbour Lane, Brookfield</li>
  </ul>
</section>

<!-- blue card front -->
<section class="sheet card card--blue" aria-label="Business card front, blue">
  <div class="brand brand--light" style="left:62px;top:60px;font-size:26px"><span class="brand-dot" style="width:20px;height:20px"></span>nexora</div>
</section>

<!-- white card back -->
<section class="sheet card card--back" aria-label="Business card back">
  <div style="position:absolute;right:0;top:0;width:70px;height:10px;background:var(--blue)"></div>
  <div class="brand" style="left:18px;top:22px;font-size:16px"><span class="brand-dot" style="width:12px;height:12px"></span>nexora</div>
  <div class="person-name" style="right:18px;top:22px">Adrian Vale</div>
  <div class="person-role" style="right:18px;top:37px">Managing Director</div>
  <ul class="contact" style="left:18px;top:72px">
    <li>+1 (555) 014 2290</li>
    <li>hello@nexora-it.com</li>
    <li>www.nexora-it.com</li>
    <li>48 Harbour Lane, Brookfield</li>
  </ul>
  <div style="position:absolute;left:0;bottom:0;width:100%;height:6px;background:var(--ink)"></div>
  <div style="position:absolute;right:0;bottom:6px;width:90px;height:5px;background:var(--blue)"></div>
</section>

<!-- letterhead -->
<section class="sheet doc letterhead" aria-label="Letterhead">
  <div class="brand" style="left:20px;top:26px;font-size:17px"><span class="brand-dot" style="width:13px;height:13px"></span>nexora</div>
  <div class="person-name" style="left:150px;top:24px;font-size:8px">Adrian Vale</div>
  <div class="person-role" style="left:150px;top:35px;font-size:5px">Managing Director</div>
  <ul class="contact" style="left:196px;top:20px;font-size:4.5px;line-height:7px;border-left:1px solid var(--blue);padding-left:5px">
    <li>+1 (555) 014 2290</li>
    <li>hello@nexora-it.com</li>
    <li>www.nexora-it.com</li>
    <li>48 Harbour Lane</li>
  </ul>
  <div class="faint-mark" role="img" aria-label="Faint brand symbol watermark" style="left:150px;top:140px;width:90px;height:90px;background:var(--faint)"></div>
  <div style="position:absolute;right:0;bottom:10px;width:90px;height:8px;background:var(--blue)"></div>
  <div style="position:absolute;left:0;bottom:4px;width:100%;height:6px;background:var(--ink)"></div>
</section>

<!-- company overview cover -->
<section class="sheet doc cover" aria-label="Client proposal cover">
  <div class="cover-panel">
    <div class="faint-mark" role="img" aria-label="Large brand symbol decoration" style="left:30px;top:40px;width:120px;height:120px;background:var(--blue-soft);opacity:.75"></div>
    <div class="cover-title">Company<br>Overview</div>
    <div class="cover-sub" style="top:183px">Lorem ipsum is simply dummy text of the printing</div>
    <div class="cover-date">August 2014</div>
  </div>
  <div class="brand" style="left:18px;top:306px;font-size:16px"><span class="brand-dot" style="width:12px;height:12px"></span>nexora</div>
  <ul class="contact" style="left:160px;top:296px;font-size:4.5px;line-height:8px;border-left:1px solid var(--blue);padding-left:5px">
    <li>+1 (555) 014 2290</li>
    <li>hello@nexora-it.com</li>
    <li>48 Harbour Lane, Brookfield</li>
  </ul>
</section>

<!-- sample text flyer -->
<section class="sheet doc flyer" aria-label="Flyer page">
  <div class="faint-mark" role="img" aria-label="Brand symbol decoration" style="left:18px;top:42px;width:62px;height:62px;background:radial-gradient(circle at 40% 35%,#4fb4e4,#0b5f8a)"></div>
  <div class="flyer-title">Sample Text</div>
  <div class="flyer-sub">Lorem ipsum is simply dummy text of the printing</div>
  <div class="flyer-body">
    <p>Lorem Ipsum is simply dummy text of the printing and typesetting industry. Lorem Ipsum has been the industry's standard dummy text ever since the 1500s, when an unknown printer took a galley of type and scrambled it to make a type specimen book. It has survived not only five centuries, but also the leap into electronic typesetting.</p>
    <p>It is a long established fact that a reader will be distracted by the readable content of a page when looking at its layout. The point of using Lorem Ipsum is that it has a more-or-less normal distribution of letters, as opposed to using content here, making it look like readable English.</p>
    <p>Contrary to popular belief, Lorem Ipsum is not simply random text. It has roots in a piece of classical Latin literature from 45 BC, making it over 2000 years old, and it was reproduced below for those interested.</p>
  </div>
  <div class="brand" style="right:18px;top:318px;font-size:14px"><span class="brand-dot" style="width:10px;height:10px"></span>nexora</div>
  <div class="rule" style="left:18px;right:18px;top:340px"></div>
  <div class="footer-line" style="left:18px;top:346px">
    <span>+1 (555) 014 2290</span><span>www.nexora-it.com</span><span>48 Harbour Lane</span>
  </div>
</section>

</body>
</html>
```